LITTLE DESIGN WORK REQUIRED!

UPDATE: WE WEREN'T OVERLY ECSTATIC WITH THE DESIGNS WE WERE RECEIVING SO WE DID MOST OF THE DESIGN WORK OURSELVES...

PLEASE SEE THE NEWLY ATTACHED PPT DOC TO VIEW NEARLY EXACT REPLICAS OF WHAT WE WANT THE SITE TO LOOK LIKE. WE NOW NEED YOUR HELP TO MAKE IT LOOK LIKE SOMETHING WORTHY OF THE WEB.

NO CODING REQUIRED - EXPECTED OUTPUT PSD FILES

Hi everyone!

We're looking for a designer to work their magic for our site! We're a not-for-profit program aimed at helping young people realise their potential!

In the attached PPT file, you'll notice we've already DESIGNED THE ENTIRE SITE IN POWERPOINT. Now, we need YOU to make the small changes we requested in the document as well as design the whole thing in psd.

Any questions, don't hesitate to ask.

Brook-Rise
Updates

We've done about 95% of the design for you. Please fine-tune it. See the newly attached PPT doc for details. 

The best two designs will win. This project closes on Friday - please message us if you are absolutely sure you cannot make the deadline.

Thanks,
Brook-Rise

```html
<!DOCTYPE html>
<html lang="en">
<head>
<meta charset="utf-8">
<title>Brook-Rise</title>
<link rel="stylesheet" href="https://fonts.googleapis.com/css2?family=Londrina+Solid:wght@400;900&family=Chewy&family=Roboto+Condensed:ital,wght@0,400;0,700;1,400&display=swap">
<style>
:root{
  --outer:#cfcfcf;
  --ink:#1c1c1c;
  --white:#ffffff;
  --stage:#ececec;
  --green:#7cb200;
  --green-dark:#5d8f00;
  --lime:#b6e01c;
  --panel:#edf1f6;
  --panel-line:#a9a9a9;
  --grey-text:#8a8a8a;
  --body-text:#7a7a7a;
  --link:#2b5ca8;
  --cyan:#29a5e0;
  --magenta:#f040e6;
  --yellow:#fbf500;
  --charcoal:#2e2e2e;
  --footer:#1d1d1d;
}
*{box-sizing:border-box;margin:0;padding:0}
html,body{width:1200px;height:1074px;overflow:hidden}
body{background:var(--outer);font-family:Arial,Helvetica,sans-serif;position:relative}
.abs{position:absolute}
.page{position:absolute;left:166px;top:0;width:860px;height:1074px;background:var(--stage)}
.topbar{left:0;top:0;width:860px;height:19px;background:var(--ink)}
.topbar .links{position:absolute;left:71px;top:5px;font-size:8px;color:#cfcfcf;letter-spacing:.5px}
.topbar .links span{margin-right:10px}
.social{display:flex;gap:4px}
.social i{display:block;width:11px;height:11px;background:#4a78b8;border-radius:2px}
.topbar .social{position:absolute;left:720px;top:4px}
.header{left:0;top:19px;width:860px;height:91px;background:var(--white);border-bottom:3px solid #d6d6d6}
.brand{position:absolute;left:81px;top:26px;display:flex;align-items:center;gap:6px;font-family:'Londrina Solid',sans-serif;font-size:26px;color:var(--ink)}
.brand b{display:block;width:18px;height:18px;border-radius:50%;background:var(--green)}
.login{position:absolute;left:545px;top:20px;font-size:8px;color:#666}
.login .row{display:flex;align-items:center;gap:5px}
.login input{width:82px;height:13px;border:1px solid #bbb}
.login .opts{display:flex;gap:90px;margin-top:7px;font-size:6px;padding-left:42px}
.login .opts span:before{content:"";display:inline-block;width:8px;height:8px;border:1px solid #bbb;margin-right:10px;vertical-align:middle}
.nav{position:absolute;left:70px;top:64px;width:728px;height:25px;border-top:2px solid var(--green);display:flex}
.nav a{font-size:9.5px;letter-spacing:1px;color:#333;padding:7px 8px;text-decoration:none}
.nav a.on{background:var(--green);color:#fff}
.search{position:absolute;right:0;top:1px;display:flex}
.search .field{width:98px;height:22px;border:1px solid #ccc;font-size:6.5px;color:#999;padding:7px 4px;background:#fff}
.search .btn{width:54px;height:22px;background:#c9c9c9;font-size:8px;color:#333;text-align:center;padding-top:7px}
.banner{left:70px;top:151px;width:728px;height:237px;border-radius:5px;overflow:hidden}
.photo{position:absolute;left:0;top:0;width:532px;height:237px;background:linear-gradient(180deg,#5f8fc7 0%,#9ab7d6 35%,#6d8b49 55%,#556c2e 100%)}
.arrow{position:absolute;top:107px;color:#fff;font-size:22px;font-weight:bold}
.promo{position:absolute;left:532px;top:0;width:196px;height:237px;background:linear-gradient(180deg,#c8f01a 0%,#8fc71a 60%,#4f8e00 100%)}
.promo .tag{position:absolute;left:8px;top:14px;background:#c4241a;color:#fff;font-family:'Londrina Solid',sans-serif;font-size:24px;padding:0 8px;border:2px solid #fff;border-radius:4px}
.promo .call{position:absolute;left:24px;top:56px;font-family:'Londrina Solid',sans-serif;font-size:31px;line-height:31px;color:#f4f11e;text-shadow:1px 1px 0 #3f7400}
.more{display:inline-block;background:#222;color:#fff;font-size:6.5px;font-weight:bold;padding:2px 6px;border-radius:2px}
.promo .more{position:absolute;left:126px;top:159px;background:#ddd;color:#333}
.card{border:1px solid var(--panel-line);border-radius:8px;background:var(--panel)}
.welcome{left:70px;top:402px;width:528px;height:273px;padding:20px 22px}
.welcome h1{font-family:'Londrina Solid',sans-serif;font-weight:900;font-size:35px;letter-spacing:1px;color:var(--green);line-height:36px}
.welcome .lead{font-size:10px;color:var(--green);line-height:16px;margin-top:14px;letter-spacing:.3px}
.welcome .lead b{font-weight:bold}
.welcome .copy{font-size:9.5px;color:var(--body-text);line-height:14.2px;margin-top:12px}
.welcome .more{position:absolute;right:20px;bottom:14px}
.side-title{font-family:'Chewy',cursive;font-size:25px;color:var(--green);text-align:center;line-height:26px}
.touch{left:606px;top:402px;width:192px;height:246px;padding:4px 10px;font-size:9px;text-align:center}
.touch label{display:block;font-weight:bold;color:#222;margin-top:8px}
.touch label em{color:#c00;font-style:normal}
.touch input{width:88px;height:15px;border:1px solid #aab;margin-top:2px}
.touch .y{background:#fdfca8}
.touch .go{display:inline-block;border:1px solid #777;background:#f2f2f2;padding:2px 6px;margin-top:6px;border-radius:2px}
.touch ul{list-style:disc;text-align:left;margin:3px 0 0 46px;color:var(--link);line-height:15px}
.touch .connect{display:inline-block;background:#4a6aa5;color:#fff;font-weight:bold;padding:2px 10px 2px 18px;border-radius:2px}
.touch .last{font-size:7.5px;color:#555;text-align:left;margin:4px 0 0 32px}
.avatars{display:flex;gap:4px;margin:3px 0 0 32px}
.avatars i{display:block;width:25px;height:25px;background:#7a7a7a}
.popular{left:606px;top:655px;width:192px;height:115px}
.popular .item{position:absolute;left:8px;top:40px;width:176px;height:52px;background:#e2e8ef}
.cal{position:absolute;left:8px;top:7px;width:29px;height:32px;background:#fff;border:1px solid #999;text-align:center;font-size:11px}
.cal span{display:block;background:#999;color:#fff;font-size:7px;height:11px}
.popular .item p{position:absolute;left:40px;top:8px;font-size:9px;font-weight:bold;color:#333;line-height:13px}
.popular .chev{position:absolute;left:88px;top:97px;width:9px;height:9px;border-right:2px solid #555;border-bottom:2px solid #555;transform:rotate(45deg)}
.amb{left:606px;top:778px;width:192px;height:171px;padding-top:5px}
.amb .side-title{font-family:'Londrina Solid',sans-serif;font-size:24px}
.person{position:absolute;left:15px;display:flex;gap:13px;font-family:'Roboto Condensed',sans-serif;color:#999}
.person .av{width:36px;height:43px;background:#9a9a9a}
.person b{display:block;font-weight:400;font-size:15px;margin-top:2px}
.person em{font-size:14px}
.tile{top:692px;width:128px;height:128px}
.tile .art{position:absolute;left:24px;top:12px;width:80px;height:80px;border-radius:6px}
.tile span{position:absolute;left:0;right:0;bottom:8px;text-align:center;font-family:'Londrina Solid',sans-serif;font-weight:900;font-size:19px;letter-spacing:1px}
.discover{left:70px;background:var(--cyan)} .discover .art{background:#4a5a6a} .discover span{color:var(--yellow)}
.design{left:204px;background:var(--magenta)} .design .art{background:#c9b8c8} .design span{color:var(--yellow)}
.build{left:337px;background:var(--yellow)} .build .art{background:#4d7fc9} .build span{color:var(--charcoal)}
.achieve{left:470px;background:var(--charcoal)} .achieve .art{background:#bfa63a} .achieve span{color:var(--magenta)}
.recent{left:73px;top:828px;font-family:'Roboto Condensed',sans-serif;font-size:21px;color:#222}
.catbar{left:70px;top:856px;width:528px;height:20px;background:var(--magenta);font-family:'Chewy',cursive;color:#fff;font-size:15px;padding-left:4px}
.postpic{left:70px;top:884px;width:263px;height:68px;border:1px solid #888;background:linear-gradient(180deg,#5d8ed0 0%,#a8c4e2 55%,#7a8da1 100%)}
.posttext{left:342px;top:886px;width:256px;font-size:9.5px;color:var(--body-text);line-height:11.5px;text-align:justify}
.footer{left:0;top:960px;width:860px;height:114px;background:var(--footer)}
.footer .copy{position:absolute;left:495px;top:52px;font-size:7.5px;color:#888}
.footer .social{position:absolute;left:627px;top:49px}
.footer .social i{background:#5a7ab0}
.footer .connect{position:absolute;left:711px;top:50px;font-size:9.5px;color:#aaa}
.footer .rule{position:absolute;left:70px;top:82px;width:728px;height:1px;background:#3a3a3a}
.footer .fnav{position:absolute;left:71px;top:92px;font-size:9px;letter-spacing:1.2px;color:#555}
.footer .fnav span{margin-right:20px}
.footer .fnav .on{color:#ddd}
</style>
</head>
<body>
<div class="page">
  <div class="abs topbar">
    <div class="links"><span>SITEMAP</span><span>FAQS</span><span>HELP</span></div>
    <div class="social"><i></i><i></i><i></i><i></i><i></i></div>
  </div>
  <header class="abs header">
    <div class="brand"><b></b>Brook-Rise</div>
    <form class="login">
      <div class="row">User Name <input> Password <input></div>
      <div class="opts"><span>Keep me logged in</span><span>Forgot password?</span></div>
    </form>
    <nav class="nav">
      <a class="on">ABOUT US</a><a>RESOURCES</a><a>WORKSHOPS</a><a>AMBASSADORS</a><a>FEATS</a>
      <div class="search"><div class="field">ENTER KEY WORD</div><div class="btn">SEARCH</div></div>
    </nav>
  </header>

  <section class="abs banner">
    <div class="photo" role="img" aria-label="Savanna scene with an elephant and calf beneath acacia trees and a mountain"></div>
    <div class="arrow" style="left:14px">&lsaquo;</div>
    <div class="arrow" style="left:506px">&rsaquo;</div>
    <div class="promo">
      <div class="tag">KILIMANJARO</div>
      <div class="call">SIGN-UP<br>FOR OUR<br>BROOK-RISE<br>FEATS</div>
      <span class="more">MORE</span>
    </div>
  </section>

  <article class="abs card welcome">
    <h1>WELCOME TO BROOK-RISE</h1>
    <p class="lead"><b>BROOK-RISE</b> is a not-for-profit program aimed at helping people – especially young people – realise their potential and achieve success.</p>
    <p class="lead"><b>OUR RESOURCES</b> are categorised into four areas: discovery, design, build, and achieve – what we believe are the four steps in the achievement framework we teach.</p>
    <p class="copy">Lorem Ipsum is simply dummy text of the printing and typesetting industry. Lorem Ipsum has been the industry's standard dummy text ever since the 1500s, when an unknown printer took a galley of type and scrambled it to make a type specimen book. It has survived not only five centuries, but also the leap into electronic typesetting, remaining essentially unchanged. It was popularised in the 1960s with the release of Typeset sheets containing Lorem Ipsum passages, and more recently with desktop publishing software like PageForge including versions of Lorem Ipsum.</p>
    <span class="more">MORE &#9656;</span>
  </article>

  <aside class="abs card touch">
    <div class="side-title">get in touch</div>
    <label>Username: <em>*</em></label><input class="y">
    <label>Password: <em>*</em></label><input>
    <div><span class="go">Log in</span></div>
    <ul><li>Create new account</li><li>Request new password</li><li><span class="connect">Connect with Friendly</span></li></ul>
    <div class="last">Last connected</div>
    <div class="avatars"><i></i><i></i><i></i><i style="background:#c9d2e6"></i></div>
  </aside>

  <aside class="abs card popular">
    <div class="side-title">whats popular</div>
    <div class="item"><div class="cal"><span>apr</span>28</div><p>Lorem ipsum eturadipcin<br>praesent vesint</p></div>
    <div class="chev"></div>
  </aside>

  <aside class="abs card amb">
    <div class="side-title">AMBASSADOR</div>
    <div class="person" style="top:48px"><div class="av" role="img" aria-label="Portrait placeholder"></div><div><b>John Doe</b><em>Young Entrepreneur</em></div></div>
    <div class="person" style="top:108px"><div class="av" role="img" aria-label="Portrait placeholder"></div><div><b>Jane Smith</b><em>Pro Athlete</em></div></div>
  </aside>

  <div class="abs tile discover"><div class="art" role="img" aria-label="Binoculars illustration"></div><span>DISCOVER</span></div>
  <div class="abs tile design"><div class="art" role="img" aria-label="Paint tube illustration"></div><span>DESIGN</span></div>
  <div class="abs tile build"><div class="art" role="img" aria-label="Blueprint and hammer illustration"></div><span>BUILD</span></div>
  <div class="abs tile achieve"><div class="art" role="img" aria-label="Trophy illustration"></div><span>ACHIVE</span></div>

  <h2 class="abs recent">Recent Posts</h2>
  <div class="abs catbar">Design</div>
  <div class="abs postpic" role="img" aria-label="Skydiver in the sky above a snowy mountain"></div>
  <p class="abs posttext">Lorem Ipsum is simply dummy text of the printing and typesetting industry. Lorem Ipsum has been the industry's standard dummy text ever since the 1500s, when an unknown printer took a galley of type and scrambled it to make a type specimen book.</p>

  <footer class="abs footer">
    <div class="copy">Brook-Rise | copyright 2012</div>
    <div class="social"><i></i><i></i><i></i><i></i><i></i></div>
    <div class="connect">Connect with us</div>
    <div class="rule"></div>
    <div class="fnav"><span class="on">ABOUT US</span><span>RESOURCES</span><span>WORKSHOPS</span><span>AMBASSADORS</span><span>FEATS</span></div>
  </footer>
</div>
</body>
</html>
```